Quendaro Pet Store Web Template

We need a new web design for an online Pet Store based in Australia but looking to expand internationally in the future.

The template HTML & CSS should be easily integrated into a quendaro web-store.

We sell a wide range of high quality pet products to our customers at competitive prices.This is our unique selling point.

We intend to become a market leader hence our brand has to look the part with simple yet outstanding icons.

The overall design has to be more visually appealing and simpler than our competitors and lead to a higher conversion rate.

The following are our biggest competitors:
www.tailnook.example
www.pawmeadow.example
www.critterloft.example

Of our competitors www.critterloft.example has the feel that we intend to have but obviously it has to be unique & iconic.

In short our web design has to be associated with Leading,Trust & Quality.

Please find attached Logo so that the site color theme can blend with the logo.

Target Market(s)

Online Pet Products shoppers worldwide

Industry/Entity Type

Pet

Coding

Coded - Design and coding required

Number of Pages Required

3 page

Font styles to use
Sans Serif

Requirements
Must have
• Check out page design.
• Product description menus(when you click on the product)
• Categories should be the same and should be hid or un-hidden by admin.
• Color theme will depend on the final logo to be completed soon.
Nice to have
• Please find attached logo.The site should blend well with logo.

```html
<!DOCTYPE html>
<html lang="en">
<head>
<meta charset="utf-8">
<title>Pawsbury Pet Store</title>
<link rel="stylesheet" href="https://fonts.googleapis.com/css2?family=Open+Sans:wght@400;600;700;800&family=Raleway:wght@300;400&display=swap">
<style>
:root{
  --green:#8cc63f;
  --green-dark:#6fa52a;
  --green-soft:#9ccf55;
  --ink:#1b1b1b;
  --black:#111;
  --text:#4d4d4d;
  --muted:#8a8a8a;
  --line:#d9e8c4;
  --white:#fff;
}
*{margin:0;padding:0;box-sizing:border-box}
html,body{width:1200px;height:2693px;overflow:hidden}
body{position:relative;background:var(--white);font-family:"Open Sans",Arial,sans-serif;color:var(--text);font-size:12px}
.abs{position:absolute}
.hero-backdrop{left:0;top:0;width:1200px;height:502px;background:linear-gradient(90deg,#5c4a3a 0%,#a88a6a 30%,#c9b59a 55%,#b28d5f 75%,#6e5a44 100%)}
.topbar{left:104px;top:0;width:967px;height:88px;color:var(--white);font-size:11px}
.cart{right:0;top:12px;display:flex;gap:14px;align-items:center}
.welcome{left:490px;top:52px}
.welcome a{color:var(--green);text-decoration:underline;margin-left:10px}
.search{left:702px;top:46px;width:265px;height:32px;display:flex}
.search input{flex:1;border:0;padding:0 8px;font:11px "Open Sans",sans-serif;color:var(--muted)}
.search button{width:34px;background:var(--black);border:0;display:flex;align-items:center;justify-content:center}
.nav{left:104px;top:88px;width:967px;height:106px;background:var(--black)}
.brand{left:0;top:0;width:230px;height:106px;display:flex;align-items:center;gap:10px;padding-left:22px;color:var(--green);font-weight:700;font-size:22px;border-right:1px solid #333}
.brand .dot{width:22px;height:22px;border-radius:50%;background:var(--green)}
.menu{left:230px;top:0;width:737px;height:32px;display:flex;font-size:12px;color:var(--white)}
.menu li{list-style:none;flex:auto;text-align:center;line-height:32px;border-right:1px solid #444}
.menu li.active{background:var(--white);color:var(--ink)}
.pets{left:230px;top:42px;display:flex;gap:0;color:var(--white);font-size:11px}
.pets li{list-style:none;width:95px;text-align:center}
.pets .ico{display:block;margin:0 auto 8px;width:16px;height:12px;border-radius:6px;background:var(--green)}
.hero{left:104px;top:194px;width:967px;height:490px;background:linear-gradient(100deg,#8a7262 0%,#d8b99a 35%,#c68c4a 60%,#a26a34 80%,#5e4a33 100%)}
.hero-copy{left:64px;top:48px;color:var(--white);font-family:Raleway,sans-serif;font-weight:300;line-height:1.05}
.hero-copy .l1{font-size:54px;letter-spacing:1px}
.hero-copy .l2{font-size:50px}
.slide-arrow{top:222px;width:20px;height:50px}
.dots{left:466px;top:458px;display:flex;gap:6px}
.dots span{width:10px;height:10px;border-radius:50%;background:var(--green)}
.dots span:first-child{background:var(--white)}
.promo{top:688px;height:215px;border:1px solid #ddd;background:var(--white)}
.promo .photo{position:absolute}
.promo h3{position:absolute;color:var(--green);font-size:19px;font-weight:700;line-height:1.1}
.promo h3 span{color:var(--ink)}
.promo p{position:absolute;font-size:11px;line-height:1.35;color:var(--text)}
.promo .more{position:absolute;width:34px;height:34px;border-radius:50%;background:var(--black);display:flex;align-items:center;justify-content:center}
.offer{top:921px;height:145px;border:3px solid #dfe6d6;background:var(--white)}
.offer .strip{position:absolute;right:0;top:0;height:24px;background:var(--green);color:var(--ink);font-size:11px;line-height:24px;padding:0 14px;left:150px}
.offer .pack{position:absolute}
.offer .name{position:absolute;font-weight:700;color:var(--ink)}
.offer .big{position:absolute;font-weight:800;color:var(--ink);line-height:1}
.blog-bar{left:104px;top:1089px;width:967px;height:56px;background:var(--green);display:flex;align-items:center;color:var(--ink);font-weight:700;font-size:18px}
.blog-bar .doc{width:72px;height:56px;background:var(--green-soft);display:flex;align-items:center;justify-content:center;margin-right:24px}
.post{top:1151px;width:410px}
.post .photo{height:212px;background:linear-gradient(180deg,#fff 0%,#f3eee8 40%,#c99d6e 70%,#fff 100%)}
.post .date{margin-top:22px;display:flex;align-items:center;gap:12px;font-size:11px}
.post .date i{width:22px;height:12px;border-radius:6px;background:var(--green)}
.post h4{margin-top:16px;font-size:13px;color:var(--ink);line-height:1.5}
.post p{margin-top:10px;font-size:11px;line-height:1.6}
.divider-v{left:594px;top:1151px;width:1px;height:380px;background:var(--line)}
.side-arrow{top:1340px}
.section-title{left:0;width:1200px;top:1588px;text-align:center;font-size:19px;font-weight:700;color:var(--ink)}
.rule{left:143px;width:856px;height:2px;background:var(--line)}
.product{top:1658px;width:200px}
.product .photo{width:110px;height:150px;margin-left:6px}
.product h5{margin-top:22px;font-size:13px;color:var(--ink)}
.product p{margin-top:6px;font-size:11px;line-height:1.5;width:140px}
.product .buy{margin-top:10px;display:flex;align-items:center;gap:10px;font-weight:700;color:var(--green);font-size:14px}
.product .buy .sep{width:40px;height:1px;background:var(--line)}
.product .sq{width:20px;height:20px;background:var(--green);display:flex;align-items:center;justify-content:center}
.product .cart-ico{width:20px;height:20px;border:1px solid var(--green)}
.help{left:104px;top:2022px;width:290px}
.help li{list-style:none;display:flex;align-items:center;gap:14px;height:64px}
.help .circle{width:52px;height:52px;border:2px solid var(--green);border-radius:50%;display:flex;align-items:center;justify-content:center;flex:none}
.help b{font-size:13px;color:var(--ink)}
.help b em{font-style:normal;color:var(--green)}
.help small{display:block;font-size:11px;color:var(--muted)}
.help-line{left:392px;top:2022px;width:2px;height:258px;background:var(--line)}
.sale{left:415px;top:2027px;width:656px;height:253px;background:linear-gradient(100deg,#2e4524 0%,#1f6f9a 30%,#c73a22 55%,#e0a52a 75%,#1f2a1a 100%)}
.sale-copy{left:470px;top:26px;color:var(--white);line-height:1}
.sale-copy .a{font-size:36px;font-weight:800}
.sale-copy .b{font-size:22px;font-weight:800;margin-top:2px}
.sale-copy .c{font-size:14px;margin-top:6px}
.sale-copy .c em{font-style:normal;color:var(--green)}
.sale-edge{right:0;top:0;width:20px;height:253px;background:var(--green);display:flex;align-items:center;justify-content:center}
.footer{left:0;top:2310px;width:1200px;height:343px;background:var(--green)}
.newsletter{left:262px;top:22px;display:flex;align-items:center;gap:28px;color:var(--white);font-weight:700;font-size:13px}
.newsletter input{width:376px;height:34px;border:0;padding:0 10px;font:11px "Open Sans",sans-serif}
.newsletter button{width:84px;height:34px;border:0;background:var(--black);color:var(--white);font:700 13px "Open Sans",sans-serif;margin-left:-28px}
.fcol{top:108px}
.fcol h6{font-size:14px;color:var(--ink);font-weight:700;margin-bottom:8px}
.fcol li{list-style:none;font-size:11px;color:var(--white);line-height:26px;display:flex;align-items:center;gap:10px}
.fcol li i{width:14px;height:10px;border-radius:4px;background:var(--white)}
.fcol li.bul::before{content:"";width:5px;height:5px;background:var(--white)}
.fbrand{left:898px;top:96px;width:190px;color:var(--white)}
.fbrand .name{display:flex;align-items:center;gap:8px;font-weight:700;font-size:20px}
.fbrand .name span{width:18px;height:18px;border-radius:50%;background:var(--white)}
.fbrand p{margin-top:14px;font-size:11px;line-height:1.45;color:var(--ink)}
.social{margin-top:18px;display:flex;gap:12px}
.social span{width:28px;height:28px;border-radius:50%;background:var(--green-dark);border:2px solid var(--white)}
.legal{left:0;top:2653px;width:1200px;height:40px;background:var(--black);color:var(--white);font-size:11px;text-align:center;line-height:40px}
</style>
</head>
<body>

<div class="abs hero-backdrop" role="img" aria-label="Blurred warm background photo of a woman with a golden retriever"></div>

<div class="abs topbar">
  <div class="abs cart">
    <svg width="16" height="14" viewBox="0 0 16 14"><path d="M1 1h3l2 8h8l1-6H5" fill="none" stroke="#fff" stroke-width="1.5"/><circle cx="7" cy="12" r="1.3" fill="#fff"/><circle cx="13" cy="12" r="1.3" fill="#fff"/></svg>
    <span>0 items</span><span>$ 00.00</span>
  </div>
  <div class="abs welcome">Welcome (Log in) <a>Your Account</a></div>
  <div class="abs search"><input value="Search"><button aria-label="Search"><svg width="14" height="14" viewBox="0 0 14 14"><circle cx="6" cy="6" r="4.3" fill="none" stroke="#fff" stroke-width="1.6"/><path d="M9 9l4 4" stroke="#fff" stroke-width="1.8"/></svg></button></div>
</div>

<header class="abs nav">
  <div class="abs brand"><span class="dot"></span>Pawsbury</div>
  <ul class="abs menu">
    <li class="active">Shop Online</li><li>Services</li><li>Loyalty Program</li><li>Pet info</li><li>Store finder</li><li>Vet services</li><li style="border:0">Blog</li>
  </ul>
  <ul class="abs pets">
    <li><i class="ico"></i>Dog</li><li><i class="ico"></i>Cat</li><li><i class="ico"></i>Fish</li><li><i class="ico"></i>Bird</li><li><i class="ico"></i>Reptile</li><li style="width:120px"><i class="ico"></i>Small Animal</li>
  </ul>
</header>

<section class="abs hero" role="img" aria-label="Photo of a smiling woman hugging a golden retriever">
  <div class="abs hero-copy"><div class="l1">YOUR PETS</div><div class="l2">Deserve the best</div></div>
  <svg class="abs slide-arrow" style="left:8px" viewBox="0 0 20 50"><path d="M16 2L4 25l12 23" fill="none" stroke="#fff" stroke-width="2"/></svg>
  <svg class="abs slide-arrow" style="right:8px" viewBox="0 0 20 50"><path d="M4 2l12 23L4 48" fill="none" stroke="#fff" stroke-width="2"/></svg>
  <div class="abs dots"><span></span><span></span><span></span></div>
</section>

<article class="abs promo" style="left:104px;width:315px">
  <div class="photo" style="left:0;top:0;width:178px;height:213px;background:linear-gradient(160deg,#3a2a22,#b07c5c 50%,#2c241f)" role="img" aria-label="Photo of a girl with her dog"></div>
  <h3 style="left:190px;top:16px">LATEST<br><span>Catalogue</span></h3>
  <p style="left:190px;top:66px;color:var(--green)">October Issue<br>Out now</p>
  <p style="left:190px;top:110px;width:115px">One of the main advantages of our commodities is their reliabilit</p>
  <div class="more" style="right:8px;bottom:8px"><svg width="12" height="8" viewBox="0 0 12 8"><path d="M1 1l5 5 5-5" fill="none" stroke="#fff" stroke-width="2"/></svg></div>
</article>

<article class="abs promo" style="left:426px;width:322px">
  <div class="photo" style="left:0;top:0;width:190px;height:213px;background:linear-gradient(160deg,#f5f0ea,#c98a5a 55%,#efe6dc)" role="img" aria-label="Photo of a child hugging a boxer dog"></div>
  <svg class="photo" style="left:232px;top:16px" width="40" height="56" viewBox="0 0 40 56"><path d="M20 2a17 17 0 0117 17c0 13-17 35-17 35S3 32 3 19A17 17 0 0120 2z" fill="#8cc63f"/><circle cx="20" cy="19" r="7" fill="#fff"/></svg>
  <h3 style="left:218px;top:84px;font-size:21px">FIND<br><span>A STORE</span></h3>
  <p style="left:218px;top:136px;width:95px;font-size:10px">Find your nearest pet showroom</p>
  <div class="more" style="right:8px;bottom:8px"><svg width="12" height="8" viewBox="0 0 12 8"><path d="M1 1l5 5 5-5" fill="none" stroke="#fff" stroke-width="2"/></svg></div>
</article>

<article class="abs promo" style="left:755px;width:316px">
  <div class="photo" style="left:0;top:0;width:314px;height:140px;background:linear-gradient(100deg,#7a5b3c,#c88b47 45%,#8a6a55 80%,#3a2c22)" role="img" aria-label="Photo of a woman cuddling a golden dog"></div>
  <h3 style="left:38px;top:146px;font-size:16px">FRIENDS <span>FOR YOUR LIFE</span></h3>
  <p style="left:38px;top:170px">Find out more about our loyalty program</p>
  <div class="more" style="right:8px;bottom:8px"><svg width="12" height="8" viewBox="0 0 12 8"><path d="M1 1l5 5 5-5" fill="none" stroke="#fff" stroke-width="2"/></svg></div>
</article>

<article class="abs offer" style="left:104px;width:476px">
  <div class="strip">Online offer only. Offer Ends 30 October 2014</div>
  <div class="pack" style="left:6px;top:10px;width:140px;height:120px;background:linear-gradient(90deg,#f2f2f2,#c3262e 40%,#f0f0f0 70%,#c3262e)" role="img" aria-label="Pet food bags and cans"></div>
  <div class="name" style="left:172px;top:42px;font-size:17px">REGAL KIBBLE</div>
  <div class="abs" style="left:164px;top:72px;font-size:11px">Super Premium Dog &amp; Cat<br><span style="padding-left:44px">Food</span></div>
  <div class="big" style="left:340px;top:34px;font-size:50px">25%<br><span style="padding-left:6px">OFF</span></div>
</article>

<article class="abs offer" style="left:594px;width:477px">
  <div class="strip" style="left:90px">Online offer only. Offer Ends 30 October 2014</div>
  <div class="big" style="left:20px;top:20px;font-size:28px">MINIMUM</div>
  <div class="big" style="left:22px;top:54px;font-size:50px">20%<br>OFF</div>
  <div class="pack" style="left:178px;top:36px;width:286px;height:90px;background:linear-gradient(90deg,#2e8b3a,#c8302c 20%,#1f5fa8 40%,#2aa0a8 55%,#2e8b3a 70%,#e59a1a 85%,#c8302c)" role="img" aria-label="Row of colourful pet food bags"></div>
</article>

<div class="abs blog-bar"><div class="doc"><svg width="24" height="30" viewBox="0 0 24 30"><path d="M2 2h14l6 6v20H2z" fill="#fff"/><path d="M6 13h12M6 18h12M6 23h9" stroke="#9ccf55" stroke-width="2"/></svg></div>the latest from our blog</div>

<svg class="abs side-arrow" style="left:104px" width="12" height="40" viewBox="0 0 12 40"><path d="M10 2L2 20l8 18" fill="none" stroke="#d9e8c4" stroke-width="2"/></svg>
<svg class="abs side-arrow" style="left:1059px" width="12" height="40" viewBox="0 0 12 40"><path d="M2 2l8 18-8 18" fill="none" stroke="#d9e8c4" stroke-width="2"/></svg>

<article class="abs post" style="left:143px">
  <div class="photo" role="img" aria-label="Group of pets: rabbit, cats, dogs and birds"></div>
  <div class="date"><i></i>Posted 20 october 2014</div>
  <h4>Lorem ipsum dolor sit amet conse ctetur adipisicing elit, sed do eiusmod tempor</h4>
  <p>Lorem ipsum dolor sit amet conse ctetur adipisicing elit, sed do eiusmod tempor incididunt ut labore et dolore magna aliqua. Ut enim ad minim veniam, quis nostrud exercitation ullamco labor-ris nisi ut aliquip ex ea commodo consequat. Duis aute irure</p>
</article>
<div class="abs divider-v"></div>
<article class="abs post" style="left:640px">
  <div class="photo" role="img" aria-label="Puppy and grey cat sitting together"></div>
  <div class="date"><i></i>Posted 20 october 2014</div>
  <h4>Lorem ipsum dolor sit amet conse ctetur adipisicing elit, sed do eiusmod tempor</h4>
  <p>Lorem ipsum dolor sit amet conse ctetur adipisicing elit, sed do eiusmod tempor incididunt ut labore et dolore magna aliqua. Ut enim ad minim veniam, quis nostrud exercitation ullamco labor-ris nisi ut aliquip ex ea commodo consequat. Duis aute irure</p>
</article>

<h2 class="abs section-title">Popular Products</h2>
<div class="abs rule" style="top:1628px"></div>

<article class="abs product" style="left:143px">
  <div class="photo" style="background:linear-gradient(135deg,#6b4a2e,#b58a5a 50%,#3f2c1c)" role="img" aria-label="Brown dog food box"></div>
  <h5>Hearth Dog food</h5>
  <p>Lorem ipsum dolor sit amet conse ctetur adipisicing elit, sed do eiusmod</p>
  <div class="buy">$ 110.00<span class="sep"></span><span class="sq"><svg width="10" height="10"><path d="M5 0v10M0 5h10" stroke="#fff" stroke-width="2"/></svg></span><span class="cart-ico"></span></div>
</article>
<article class="abs product" style="left:380px">
  <div class="photo" style="background:linear-gradient(135deg,#1d5fae,#f3c21a 50%,#1d5fae)" role="img" aria-label="Blue puppy food bag"></div>
  <h5>Pup Crunch</h5>
  <p>Lorem ipsum dolor sit amet conse ctetur adipisicing elit, sed do eiusmod</p>
  <div class="buy">$ 125.00<span class="sep"></span><span class="sq"><svg width="10" height="10"><path d="M5 0v10M0 5h10" stroke="#fff" stroke-width="2"/></svg></span><span class="cart-ico"></span></div>
</article>
<article class="abs product" style="left:617px">
  <div class="photo" style="background:linear-gradient(135deg,#c8651e,#e89a4a 50%,#8a3f12)" role="img" aria-label="Orange animal food bag"></div>
  <h5>Nova Animal food</h5>
  <p>Lorem ipsum dolor sit amet conse ctetur adipisicing elit, sed do eiusmod</p>
  <div class="buy">$ 105.00<span class="sep"></span><span class="sq"><svg width="10" height="10"><path d="M5 0v10M0 5h10" stroke="#fff" stroke-width="2"/></svg></span><span class="cart-ico"></span></div>
</article>
<article class="abs product" style="left:870px">
  <div class="photo" style="background:linear-gradient(135deg,#d6317a,#2a9fb0 55%,#d6317a)" role="img" aria-label="Pink and teal pet food bag"></div>
  <h5>Vitanova</h5>
  <p>Lorem ipsum dolor sit amet conse ctetur adipisicing elit, sed do eiusmod</p>
  <div class="buy">$ 105.00<span class="sep"></span><span class="sq"><svg width="10" height="10"><path d="M5 0v10M0 5h10" stroke="#fff" stroke-width="2"/></svg></span><span class="cart-ico"></span></div>
</article>

<div class="abs rule" style="top:1981px"></div>

<ul class="abs help">
  <li><span class="circle"><svg width="26" height="18" viewBox="0 0 26 18"><path d="M1 2h14v11H1zM15 6h6l4 4v3h-10" fill="none" stroke="#8cc63f" stroke-width="2"/><circle cx="6" cy="15" r="2" fill="#8cc63f"/><circle cx="20" cy="15" r="2" fill="#8cc63f"/></svg></span><div><b><em>Delivery</em> information</b><small>View Details »</small></div></li>
  <li><span class="circle"><svg width="22" height="22" viewBox="0 0 22 22"><path d="M4 11a7 7 0 1 0 2-5" fill="none" stroke="#8cc63f" stroke-width="2"/><path d="M3 2v6h6" fill="none" stroke="#8cc63f" stroke-width="2"/></svg></span><div><b><em>Return</em> Query</b><small>View Details »</small></div></li>
  <li><span class="circle"><svg width="18" height="24" viewBox="0 0 18 24"><path d="M9 1a8 8 0 018 8c0 6-8 14-8 14S1 15 1 9a8 8 0 018-8z" fill="none" stroke="#8cc63f" stroke-width="2"/><circle cx="9" cy="9" r="3" fill="#8cc63f"/></svg></span><div><b><em>Questions?</em> View FAQs</b><small>View Details »</small></div></li>
  <li><span class="circle"><svg width="22" height="22" viewBox="0 0 22 22"><path d="M5 2l4 4-2 3c1 3 3 5 6 6l3-2 4 4-3 3C9 20 2 13 2 5z" fill="#8cc63f"/></svg></span><div><b><em>Let us Help</em> Contact us</b><small>View Details »</small></div></li>
</ul>
<div class="abs help-line"></div>

<section class="abs sale" role="img" aria-label="Photo of a colourful macaw parrot">
  <div class="abs sale-copy"><div class="a">BIRD</div><div class="b">PRODUCT SALE</div><div class="c"><em>900 items</em> available</div></div>
  <div class="abs sale-edge"><svg width="8" height="14" viewBox="0 0 8 14"><path d="M1 1l6 6-6 6" fill="none" stroke="#fff" stroke-width="2"/></svg></div>
</section>

<footer class="abs footer">
  <div class="abs newsletter">NEWS LETTER <input value="Enter your E - mail address"><button>Submit</button></div>
  <div class="abs fcol" style="left:104px"><h6>Shop Now</h6><ul><li><i></i>Dog</li><li><i></i>Cat</li><li><i></i>Fish</li><li><i></i>Bird</li><li><i></i>Reptile</li><li><i></i>Small Animal</li></ul></div>
  <div class="abs fcol" style="left:288px"><h6>Services</h6><ul><li class="bul">Grooming</li><li class="bul">Adoption</li><li class="bul">Dog wash</li><li class="bul">Hotel</li><li class="bul">Puppy School</li></ul></div>
  <div class="abs fcol" style="left:472px"><h6>Shopping Online</h6><ul><li class="bul">Contact Us</li><li class="bul">Delivery Information</li><li class="bul">Security Policy</li><li class="bul">Privacy Policy</li><li class="bul">Returns Policy</li><li class="bul">Condition of Use</li><li class="bul">FAQs</li></ul></div>
  <div class="abs fcol" style="left:677px"><h6>About Us</h6><ul><li class="bul">About Us</li><li class="bul">Careers</li><li class="bul">Pet info</li><li class="bul">Loyalty Program</li><li class="bul">Price Pledge</li><li class="bul">Contact Us</li></ul></div>
  <div class="abs fbrand">
    <div class="name"><span></span>Pawsbury</div>
    <p>Lorem ipsum dolor sit amet conse ctetur adipisicing elit, sed do eiusmod</p>
    <div class="social"><span></span><span></span><span></span><span></span></div>
  </div>
</footer>
<div class="abs legal">© 2014 - Privacy policy</div>

</body>
</html>
```